依頼詳細
サイト構成・基本的な要件については
https://zuvexo.example/boards/R7pQ2mXa9TkWvHcY/B58F3
をご参照ください。

ただ、レイアウトについては、各コンテンツへの導線が確保されていれば、
上記レイアウト案を必ず守る必要はございません。
また、当方jqueryを使用したコーディングも可能です。

提出の写真素材は
https://qlbox.example/T9wRkA
上記のものをご利用いただければ幸いです。

現在、素材があまり集まっていないため、
http://fotmira.example/
などから、10000円程度までならこちらにて購入可能です。
カンプデータにて作成頂き、納品時に当方にて購入したデータに差し替えていただければと存じます。

https://images.velonta.example/jp/
についても定期購入しておりますので、
5点ほどでしたら取得可能です。

また、既存サイト
https://www.harimoku.example/
に使用されている画像は自由にご利用ください。

【参考サイト】
https://www.tzr-worldwide.example/jp/
https://morifusa.example/
https://hotarubako.example/
https://www.calmfield.example/
https://www.yosetabi.example/

写真を大きく見せ、
高級感があり、訴求力の高いデザインを希望します。

色合いは、現在のサイト同様、
モノトーンをベースに、差し色を使用する場合は1色程度、
シックで高級感のある色合いを希望いたします。
サイトURL
ページ数
1ページ
希望イメージ
シンプル 複雑
単色 カラフル
暗い 明るい
日常 高級
遊び心 厳粛
未来的 伝統的
女性的 男性的
希望する色
グレー系
納品ファイル
• 高解像度JPG (.jpg)
• フォトショップ形式 (.psd)
補足説明
提出の写真素材は
https://qlbox.example/T9wRkA
上記アップロードしたものをご利用いただければ幸いです。

現在、素材があまり集まっていないため、
http://fotmira.example/
についても定期購入しておりますので、
5点ほどでしたら取得可能です。

納品データはPSDのほか
XDの提出でも問題ございません。

制作に関してご不明な点がございましたら
お気軽にお申し付けください。

何卒宜しくお願い致します。

```html
<!DOCTYPE html>
<html lang="ja">
<head>
<meta charset="utf-8">
<title>株式会社 ハリモク</title>
<link href="https://fonts.googleapis.com/css2?family=Jost:wght@300;400;500&family=Noto+Sans+JP:wght@300;400;500;700&display=swap" rel="stylesheet">
<style>
:root{
  --bg:#eeeff1;
  --white:#ffffff;
  --ink:#2b2b2b;
  --sub:#6d6d6d;
  --dark:#262626;
  --accent:#4a7db3;
  --line:#cfd2d6;
}
*{margin:0;padding:0;box-sizing:border-box}
html,body{width:1200px;height:3620px;overflow:hidden}
body{background:var(--bg);color:var(--ink);font-family:"Noto Sans JP",sans-serif;position:relative}
.abs{position:absolute}
.photo{position:absolute}
.en{font-family:"Jost",sans-serif;letter-spacing:.12em}

/* header & hero */
.hero{left:0;top:0;width:1200px;height:620px;background:linear-gradient(120deg,#c9c6c1 0%,#e4e1dc 40%,#b9b3ab 70%,#5e5650 100%)}
.logo{left:16px;top:0;width:104px;height:84px;background:#3b4c5f;color:#fff;display:flex;align-items:center;justify-content:center;gap:6px;font-size:13px;font-weight:500}
.logo i{width:8px;height:8px;background:#fff;display:block}
.nav{left:440px;top:14px;display:flex;gap:34px;font-size:11px;color:#fff}
.tel-box{left:950px;top:0;width:120px;height:40px;background:var(--dark);color:#fff;font-size:12px;padding:6px 10px;line-height:1.3}
.tel-box small{font-size:8px;display:block;color:#bbb}
.head-cta{left:1074px;top:0;width:110px;height:40px;background:var(--accent);color:#fff;font-size:11px;display:flex;align-items:center;justify-content:center}
.hero-title{left:140px;top:270px;color:#fff;font-size:44px;font-weight:700;letter-spacing:.08em}
.hero-lead{left:140px;top:340px;color:#fff;font-size:12px;line-height:1.9;width:440px}

/* about */
.sec-title{font-family:"Jost",sans-serif;font-size:34px;letter-spacing:.1em;font-weight:400}
.sec-sub{font-size:10px;color:var(--sub);letter-spacing:.2em}
.about-bg{left:0;top:620px;width:1200px;height:800px;background:var(--white)}
.about-text{left:700px;top:810px;width:440px;font-size:11px;line-height:2;color:var(--sub)}
.concept{left:0;top:1060px;width:600px;height:340px;background:var(--dark);color:#fff;padding:60px 50px}
.concept h3{font-size:19px;font-weight:500;line-height:1.6;margin-bottom:26px}
.concept p{font-size:11px;line-height:2;color:#cfcfcf}

/* works */
.center{width:1200px;text-align:center}
.work{position:absolute;width:272px;height:160px}
.work span{position:absolute;left:50%;bottom:14px;transform:translateX(-50%);background:#fff;font-size:10px;padding:5px 16px;white-space:nowrap}
.btn{position:absolute;border:1px solid var(--ink);font-size:11px;display:flex;align-items:center;justify-content:center;gap:10px;background:var(--white)}

/* contact */
.contact{left:200px;top:2960px;width:820px;height:200px;background:var(--white);overflow:hidden}
.contact .ghost{position:absolute;right:-10px;bottom:-24px;font-family:"Jost",sans-serif;font-size:110px;color:#eceef0;letter-spacing:.08em}
.c-btn{position:absolute;background:var(--accent);color:#fff;font-size:12px;display:flex;align-items:center;justify-content:center}

/* news */
.news{left:200px;top:3200px;width:820px;height:180px;background:var(--white)}
.news ul{list-style:none;position:absolute;left:210px;top:30px;width:560px}
.news li{font-size:11px;padding:10px 0;border-bottom:1px solid var(--line);display:flex;gap:40px}
.news li b{font-weight:400;color:var(--sub);font-family:"Jost",sans-serif}

/* footer */
.footer{left:0;top:3396px;width:1200px;height:224px;background:var(--dark);color:#fff}
.footer .name{position:absolute;left:200px;top:36px;font-size:18px;font-weight:500}
.footer .addr{position:absolute;left:200px;top:74px;font-size:10px;line-height:1.8;color:#bdbdbd}
.footer .f-btn{position:absolute;left:200px;top:146px;width:160px;height:30px;background:var(--accent);font-size:10px;display:flex;align-items:center;justify-content:center}
.f-links{position:absolute;left:620px;top:40px;display:grid;grid-template-columns:repeat(3,140px);row-gap:26px;font-size:10px;color:#ddd}
.copy{position:absolute;left:0;bottom:10px;width:1200px;text-align:center;font-size:9px;color:#8a8a8a}
</style>
</head>
<body>

<!-- hero -->
<div class="abs hero" role="img" aria-label="明るいリビングの写真：赤いソファと黒いラウンジチェア、大きな窓"></div>
<div class="abs logo"><i></i>HARIMOKU</div>
<nav class="abs nav"><span>トップページ</span><span>施工事例</span><span>よくある質問</span><span>会社案内</span><span>お知らせ</span><span>採用情報</span></nav>
<div class="abs tel-box"><small>受付 9:00〜18:00</small>0120-418-552</div>
<div class="abs head-cta">お問い合わせ</div>
<h1 class="abs hero-title">快適居住空間の演出</h1>
<p class="abs hero-lead">ハリモクは住まいの新築・リフォーム・インテリアまで、<br>お客様の理想の空間を丁寧に形にし、心地よい暮らしをご提案いたします。</p>

<!-- about -->
<div class="abs about-bg"></div>
<div class="photo" style="left:0;top:640px;width:600px;height:420px;background:linear-gradient(135deg,#5a544c,#a89c8c 50%,#3b3a38)" role="img" aria-label="キッチンとダイニングのある室内写真"></div>
<div class="abs" style="left:700px;top:710px"><div class="sec-title">ABOUT US</div><div class="sec-sub">ハリモクについて</div></div>
<p class="abs about-text">ハリモクは創業以来、住まいづくりを通してお客様の暮らしに寄り添ってまいりました。設計から施工、アフターサービスまで一貫した体制で、上質で快適な空間をお届けします。<br><br>素材選びから細部の仕上げまでこだわり、長く愛される住まいを目指しています。</p>
<div class="abs concept">
  <h3>ハリモクは多数物件を手がけ、<br>一人ひとりにあった住空間をご提案しています</h3>
  <p>お客様のご要望を丁寧にお伺いし、間取りや素材、照明まで総合的にご提案いたします。戸建てからマンション、店舗まで幅広い実績がございます。<br><br>経験豊富なスタッフが、理想の空間づくりを最後までサポートいたします。</p>
</div>
<div class="photo" style="left:600px;top:1120px;width:600px;height:260px;background:linear-gradient(120deg,#e9e4dc,#c8bba8 55%,#8d7d68)" role="img" aria-label="白いソファのある明るいリビング写真"></div>

<!-- works -->
<div class="abs center" style="top:1470px"><div class="sec-title">WORKS</div><div class="sec-sub">様々なご要望にお応えし、多数施工を手掛けております</div></div>
<div class="work" style="left:28px;top:1560px;background:linear-gradient(135deg,#4e4a44,#b7ada0)" role="img" aria-label="施工事例写真"><span>デザインリフォーム</span></div>
<div class="work" style="left:320px;top:1560px;background:linear-gradient(135deg,#2f2f31,#9c9a98)" role="img" aria-label="施工事例写真"><span>マンションリフォーム</span></div>
<div class="work" style="left:612px;top:1560px;background:linear-gradient(135deg,#d8d5d0,#8f8b85)" role="img" aria-label="施工事例写真"><span>店舗・事務所リフォーム</span></div>
<div class="work" style="left:904px;top:1560px;background:linear-gradient(135deg,#ddd8d0,#a9a196)" role="img" aria-label="施工事例写真"><span>子ども部屋</span></div>
<div class="work" style="left:28px;top:1740px;background:linear-gradient(135deg,#8c8983,#d2cec8)" role="img" aria-label="施工事例写真"><span>水廻りリフォーム</span></div>
<div class="work" style="left:320px;top:1740px;background:linear-gradient(135deg,#6b4a2c,#c08a52)" role="img" aria-label="施工事例写真"><span>エクステリア</span></div>
<div class="work" style="left:612px;top:1740px;background:linear-gradient(135deg,#2a2420,#8a5a34)" role="img" aria-label="施工事例写真"><span>ショップ・オフィス</span></div>
<div class="work" style="left:904px;top:1740px;background:linear-gradient(135deg,#e0d7ca,#b39c80)" role="img" aria-label="施工事例写真"><span>和室リフォーム</span></div>
<div class="btn" style="left:480px;top:2000px;width:240px;height:40px">施工事例をすべて見る <span>›</span></div>

<!-- recent works -->
<div class="abs center" style="top:2130px"><div class="sec-title">RECENT WORKS</div><div class="sec-sub">最新施工例</div></div>
<div class="photo" style="left:192px;top:2220px;width:360px;height:230px;background:linear-gradient(160deg,#1c2230,#4a4a58 60%,#2a2a2a)" role="img" aria-label="夜景の見えるリビングの写真"></div>
<div class="photo" style="left:560px;top:2220px;width:460px;height:230px;background:linear-gradient(160deg,#9aa6b2,#4d4d50 60%,#1f1f1f)" role="img" aria-label="窓際の黒いソファのある部屋の写真"></div>
<div class="photo" style="left:192px;top:2458px;width:404px;height:360px;background:linear-gradient(135deg,#e4e2df,#b7b1a9 60%,#7b7168)" role="img" aria-label="明るいダイニングキッチンの写真"></div>
<div class="photo" style="left:604px;top:2458px;width:416px;height:360px;background:linear-gradient(135deg,#f0ede8,#c7bcae 55%,#4a4540)" role="img" aria-label="白を基調としたリビングの写真"></div>
<div class="btn" style="left:480px;top:2870px;width:240px;height:40px">最新施工例をもっと見る <span>›</span></div>

<!-- contact -->
<div class="abs contact">
  <div class="ghost">CONTACT</div>
  <div class="abs" style="left:60px;top:50px"><div class="sec-title" style="font-size:28px">CONTACT</div><div class="sec-sub">お問い合わせ</div></div>
  <p class="abs" style="left:60px;top:120px;font-size:10px;color:var(--sub)">お気軽にお問い合わせください</p>
  <div class="abs" style="left:380px;top:56px;font-size:13px;line-height:1.6"><span class="en" style="font-size:18px;letter-spacing:.04em">Tel. 0120-418-552</span><br><small style="font-size:9px;color:var(--sub)">受付時間 9:00〜18:00</small></div>
  <div class="c-btn" style="left:580px;top:56px;width:190px;height:44px">お問い合わせはこちら ›</div>
</div>

<!-- news -->
<div class="abs news">
  <div class="abs" style="left:60px;top:30px"><div class="sec-title" style="font-size:26px">NEWS</div><div class="sec-sub">お知らせ</div></div>
  <div class="btn" style="left:60px;top:110px;width:90px;height:26px;font-size:10px">MORE ›</div>
  <ul>
    <li><b>2020.08.27</b>夏季休業のお知らせ</li>
    <li><b>2020.08.17</b>ホームページを公開しました</li>
    <li><b>2020.07.21</b>新しい施工事例を追加しました</li>
    <li><b>2020.06.10</b>相談会開催のご案内を掲載しました</li>
  </ul>
</div>

<!-- footer -->
<footer class="abs footer">
  <div class="name">株式会社 ハリモク</div>
  <div class="addr">〒000-0000<br>東京都架空区見本町1丁目2番3号 サンプルビル4F<br>Tel. 0120-418-552</div>
  <div class="f-btn">お問い合わせはこちら ›</div>
  <div class="f-links">
    <span>トップページ</span><span>施工事例</span><span>お問い合わせ</span>
    <span>会社案内</span><span>お知らせ</span><span>プライバシー</span>
    <span>よくある質問</span><span>採用情報</span><span>サイトマップ</span>
  </div>
  <div class="copy">Copyright © HARIMOKU Co.,Ltd. All Rights Reserved.</div>
</footer>

</body>
</html>
```